Wohnungsbaugenossenschaft sucht Webdesign
Zielgruppe
es geht um eine Wohnungsbaugenossenschaft, die Wohnungen an unterschiedlichen Standorten vermietet. Die Webseite soll die WBG präsentieren. Einerseits sollen die Mieter über 'Laufendes' informiert werden, andereseits sollen aktuelle Mietangebote mittels externen Link für potentielle Mieter angezeigt werden.
Aufgabenstellung
Logo, siehe Dateiupload, die Seite muss aber nicht unbedingt 'grün' sein. Diverse Fotos siehe Dateiupload (müssen nicht alle verwendet werden). Texte siehe jetzige Webseite, es können auch LoremIpsum verwendet werden.
Es soll nur die Startseite gelayoutet werden.

```html
<!DOCTYPE html>
<html lang="de">
<head>
<meta charset="utf-8">
<title>AnTa RuMo – Startseite</title>
<link href="https://fonts.googleapis.com/css2?family=Didact+Gothic&family=Montserrat:wght@500;600;700&display=swap" rel="stylesheet">
<style>
:root{
  --green:#1b8a42;
  --green-dark:#157535;
  --text:#333333;
  --muted:#666666;
  --topbar:#ececec;
  --rule:#d6d6d6;
  --footer:#e4e4e2;
  --white:#ffffff;
}
*{margin:0;padding:0;box-sizing:border-box}
html,body{width:1200px;height:2404px;overflow:hidden;background:var(--white)}
body{position:relative;font-family:"Didact Gothic",sans-serif;color:var(--text)}
.abs{position:absolute}
.topbar{left:0;top:0;width:1200px;height:34px;background:var(--topbar);font-size:12px;color:var(--muted)}
.topbar .hours{left:52px;top:10px}
.topbar .mail{left:630px;top:10px}
.topbar .lang{left:1090px;top:10px;letter-spacing:1px}
.topbar .home{left:1030px;top:8px}
.header{left:0;top:34px;width:1200px;height:166px;background:var(--white)}
.brand{left:52px;top:78px;display:flex;align-items:center;gap:12px;font-family:"Montserrat",sans-serif;font-weight:700;font-size:38px;color:var(--green)}
.brand .mark{width:30px;height:30px;background:var(--green)}
.nav{left:346px;top:134px;display:flex;gap:0;font-family:"Montserrat",sans-serif;font-weight:600;font-size:14px;color:#444;letter-spacing:.3px}
.nav a{color:inherit;text-decoration:none;margin-right:36px}
.nav a.active{color:var(--green)}
.nav-indicator{left:344px;top:198px;width:92px;height:10px;background:var(--green)}
.header-rule{left:0;top:200px;width:1200px;height:10px;background:var(--rule)}
.hero{left:0;top:210px;width:1200px;height:620px;background:linear-gradient(180deg,#9a8ea6 0%,#c9a9a4 30%,#7d8189 55%,#5f6a66 80%,#4e6a3b 100%)}
.hero-title{left:0;top:430px;width:1556px;text-align:center;font-family:"Montserrat",sans-serif;color:var(--white);line-height:1}
.hero-title .l1{position:absolute;left:0;width:100%;top:10px;font-size:33px;font-weight:500}
.hero-title .l2{position:absolute;left:0;width:100%;top:72px;font-size:36px;font-weight:600}
.hero-title .l3{position:absolute;left:0;width:100%;top:142px;font-size:33px;font-weight:500}
.btn{display:flex;align-items:center;justify-content:center;background:var(--green);color:var(--white);font-family:"Montserrat",sans-serif;font-weight:700;text-decoration:none}
.hero-btn{left:877px;top:632px;width:244px;height:66px;font-size:27px}
.about-img{left:32px;top:896px;width:662px;height:411px;background:linear-gradient(135deg,#dfe8de 0%,#f1f1ef 40%,#c9c4bb 100%)}
.about{left:722px;top:896px;width:422px}
.section-title{font-family:"Montserrat",sans-serif;font-weight:700;color:var(--green);font-size:26px}
.about p{font-size:16px;line-height:22.5px;text-align:justify;margin-top:14px}
.about p+p{margin-top:22px}
.about-btn{left:823px;top:1234px;width:242px;height:66px;font-size:25px}
.offers-title{left:0;top:1360px;width:1200px;text-align:center}
.offers-lead{left:215px;top:1418px;width:770px;text-align:center;font-size:16px;line-height:22px}
.card-img{top:1513px;height:340px}
.card-img.a{left:32px;width:371px;background:linear-gradient(180deg,#3e77c8 0%,#8fb0d8 35%,#cfc8b2 60%,#a69d85 100%)}
.card-img.b{left:416px;width:364px;background:linear-gradient(180deg,#6b7d62 0%,#8e8f8a 30%,#e9e6e0 55%,#b6b0a2 100%)}
.card-img.c{left:795px;width:371px;background:linear-gradient(180deg,#3a6fc4 0%,#9cb4d6 30%,#e4e2de 60%,#b7b0a5 100%)}
.card-text{top:1872px;font-size:15.5px;line-height:20px;text-align:center}
.card-text.a{left:32px;width:371px}
.card-text.b{left:416px;width:364px}
.card-text.c{left:795px;width:371px}
.card-btn{top:1961px;width:174px;height:68px;font-size:29px}
.card-btn.a{left:127px}.card-btn.b{left:510px}.card-btn.c{left:895px}
.footer{left:0;top:2122px;width:1200px;height:282px;background:var(--footer)}
.footer-info{left:81px;top:2150px;font-size:18px;line-height:38px;color:#555}
.footer-info .gap{height:16px}
.footer-info .row{display:flex;align-items:center;gap:10px}
.footer-info svg{width:16px;height:16px}
.footer-links{left:718px;top:2150px;font-size:18px;line-height:39px;color:#555}
.footer-links a{display:block;color:inherit;text-decoration:none}
.footer-map{left:896px;top:2152px;width:267px;height:124px;background:linear-gradient(135deg,#eef2ea,#dfe5d8)}
</style>
</head>
<body>
<div class="abs topbar">
  <span class="abs hours">Sprechtage: Di 09:00 – 12:00 Uhr und Do 13:00 – 16:00</span>
  <span class="abs mail">info@anta-rumo.example</span>
  <svg class="abs home" width="18" height="18" viewBox="0 0 18 18" fill="none" stroke="#666" stroke-width="1.6"><path d="M2 9 9 3l7 6M4 8v7h4v-4h2v4h4V8"/></svg>
  <span class="abs lang">DE | EN</span>
</div>

<header class="abs header">
  <div class="abs brand" style="top:44px"><span class="mark"></span>AnTa RuMo</div>
  <nav class="abs nav" style="top:100px">
    <a class="active" href="#">STARTSEITE</a>
    <a href="#">MIETANGEBOTE</a>
    <a href="#">GENOSSENSCHAFT</a>
    <a href="#">NEUIGKEITEN</a>
    <a href="#">NOTDIENST</a>
    <a href="#">KONTAKT</a>
  </nav>
</header>
<div class="abs header-rule"></div>
<div class="abs nav-indicator"></div>

<section class="abs hero" role="img" aria-label="Foto eines Einfamilienhauses in der Abenddämmerung"></section>
<div class="abs hero-title">
  <span class="l1">Herzlich Willkommen bei der</span>
  <span class="l2">Wohnungsbaugenossenschaft AnTa</span>
  <span class="l3">eG RuMo</span>
</div>
<a class="abs btn hero-btn" href="#">Jetzt ansehen</a>

<div class="abs about-img" role="img" aria-label="Foto eines Handschlags über einem Schreibtisch mit Vertrag"></div>
<section class="abs about">
  <h2 class="section-title">ÜBER UNS</h2>
  <p>Wir sind seit 1926 eine eingetragene Genossenschaft und verwalten zur Zeit ca. 456 Wohneinheiten.<br>Neben Mehrfamilienhäusern verwalten wir auch Ein- und Zweifamilienhäuser.<br>Alle Wohnungsstandorte sind rund um das malerische RuMo gelegen. Die ganze Region gehört zum wunderschönen Bergland.</p>
  <p>Lassen auch Sie sich von dieser schönen Wohngegend verzaubern.</p>
</section>
<a class="abs btn about-btn" href="#">Mehr erfahren</a>

<h2 class="abs section-title offers-title">MIETANGEBOTE</h2>
<p class="abs offers-lead">Die Wohngebäude befinden sich meist in Stadtrandlage, Siedlungen, an Einzelstandorten und sind von Park- und Grünanlagen umgeben.</p>

<div class="abs card-img a" role="img" aria-label="Foto eines mehrgeschossigen Altbau-Wohnhauses"></div>
<div class="abs card-img b" role="img" aria-label="Foto eines hellen Mehrfamilienhauses mit Grauschieferdach"></div>
<div class="abs card-img c" role="img" aria-label="Foto eines zweigeschossigen Wohnblocks"></div>

<p class="abs card-text a">Lorem ipsum dolor sit amet, consectetur adipisicing elit, sed do eiusmod tempor incididunt ut labore et dolore magna aliqua. Ut enim ad</p>
<p class="abs card-text b">Lorem ipsum dolor sit amet, consectetur adipisicing elit, sed do eiusmod tempor incididunt ut labore et dolore magna</p>
<p class="abs card-text c">Lorem ipsum dolor sit amet, consectetur adipisicing elit, sed do eiusmod tempor incididunt ut labore et dolore magna</p>

<a class="abs btn card-btn a" href="#">Mieten</a>
<a class="abs btn card-btn b" href="#">Mieten</a>
<a class="abs btn card-btn c" href="#">Mieten</a>

<footer class="abs footer">
  <div class="abs footer-info" style="top:28px;left:81px">
    <div>Wohnungsbaugenossenschaft AnTa eG RuMo</div>
    <div>Lindenweg 4</div>
    <div>01234 RuMo</div>
    <div class="gap"></div>
    <div class="row"><svg viewBox="0 0 16 16" fill="#666"><path d="M3 1h3l1.5 4-2 1.5a9 9 0 0 0 4 4L11 8.5l4 1.5v3a2 2 0 0 1-2 2A12 12 0 0 1 1 3a2 2 0 0 1 2-2z"/></svg>(01234) 55501</div>
    <div class="row"><span style="width:16px"></span>(01234) 555602</div>
    <div class="row"><svg viewBox="0 0 16 16" fill="none" stroke="#666" stroke-width="1.6"><path d="M2 10V8a6 6 0 0 1 12 0v2"/><rect x="1.5" y="9" width="3" height="5" fill="#666"/><rect x="11.5" y="9" width="3" height="5" fill="#666"/></svg>(01234) 555 603</div>
  </div>
  <nav class="abs footer-links" style="top:20px;left:718px">
    <a href="#">Kontakt</a>
    <a href="#">Impressum</a>
    <a href="#">Datenschutz</a>
    <a href="#">FAQ</a>
  </nav>
  <div class="abs footer-map" style="top:30px" role="img" aria-label="Lageplan mit Straßen und markiertem Standort"></div>
</footer>
</body>
</html>
```